Denver-based business coaching & networking business needs marketing postcard design

We need help designing an oversized postcard that our sales team can use as a leave-behind when they are talking to different businesses and professionals. We have a program that has business owners and sales professionals attend a one day seminar to develop an executable business plan online that is ready to be implemented. Following the seminar they participate in bi-weekly group meetings where they collaborate with other professionals, review and stay accountable to their plan, and pass referrals. We would like to have a few graphics included from our website (www.trelvany.com) including the Map-Build-Connect graphic and the "Six Traps That Sink Strategies" graphic. The final design should be able to have a clear call-to-action about attending a seminar to begin their journey with Trelvany.

Language we would like to have included is as follows:

Learn Business Strategy
Create an Executable Business Plan
Receive Consistent Coaching
Attend Additional Educational Sessions
Profit from Peer Collaboration
Stay Accountable through Bi-Weekly Meetings
Increase your income through Referrals

The role of Trelvany is to develop successful business people through education, collaboration and community. This is created by first attending a one day seminar whose purpose is to assist attendees in creating an immediately executable business plan. Attendees then meet bi-weekly to pass referrals, collaborate on challenges and continually check in on their own plans, to ensure their continued success.

Target Market(s)

Age 28-45, Realtors, Mortgage Brokers, Insurance Professionals, Financial Advisors, CPA's, Attorneys, Small Business Owners

Industry/Entity Type

Business Consultant

Font styles to use
Sans Serif

Colors
faa54b
f37122

Requirements
Must have
• Trelvany logo, text that was provided in description, graphics that hit on elements from our website, call to action, website address

```html
<!DOCTYPE html>
<html lang="en">
<head>
<meta charset="utf-8">
<title>Trelvany Postcard</title>
<link rel="stylesheet" href="https://fonts.googleapis.com/css2?family=Open+Sans:wght@400;600;700&display=swap">
<style>
  :root{
    --orange:#f37122;
    --orange-light:#faa54b;
    --grey-text:#5b5b5b;
    --grey-dark:#3d3d3d;
    --paper:#ffffff;
    --canvas:#e9e9e9;
    --social:#f7a46a;
  }
  *{box-sizing:border-box;margin:0;padding:0}
  html,body{width:900px;height:1200px;overflow:hidden}
  body{background:var(--canvas);font-family:"Open Sans",Arial,sans-serif;color:var(--grey-text);position:relative}
  .card{position:absolute;left:40px;width:820px;height:512px;background:var(--paper);box-shadow:0 4px 14px rgba(0,0,0,.18);overflow:hidden}
  .card--front{top:48px}
  .card--back{top:640px}

  .brand{position:absolute;top:20px;left:28px;display:flex;align-items:center;gap:10px}
  .brand__mark{width:30px;height:30px;background:var(--orange)}
  .brand__name{font-weight:700;font-size:34px;letter-spacing:.5px;color:var(--grey-text);text-transform:uppercase;line-height:1}

  .tagline{position:absolute;top:28px;right:30px;font-size:22px;font-weight:600;color:var(--orange);letter-spacing:.5px}

  .hero{position:absolute;top:76px;left:0;width:820px;height:290px}
  .hero__photo{position:absolute;inset:0;background:linear-gradient(110deg,#f28a3c 0%,#f7a25a 45%,#f9c28c 70%,#f5a866 100%)}
  .hero__tint{position:absolute;inset:0;background:linear-gradient(90deg,rgba(243,113,34,.85) 0%,rgba(243,113,34,.55) 60%,rgba(250,165,75,.35) 100%)}
  .hero__copy{position:absolute;top:18px;left:28px;width:740px;color:#fff;font-size:12.5px;line-height:1.45}
  .hero__lead{margin-top:14px;font-weight:600}

  .reasons{position:absolute;left:28px;right:28px;top:140px;display:flex;gap:22px}
  .reason{flex:1;text-align:center;color:#fff}
  .reason__icon{height:62px;display:flex;align-items:center;justify-content:center;border-bottom:1px solid rgba(255,255,255,.6)}
  .reason__text{margin-top:10px;background:rgba(243,113,34,.85);padding:10px 8px;font-size:11.5px;line-height:1.35;min-height:48px}

  .approach{position:absolute;top:392px;left:28px;font-size:24px;color:var(--orange);line-height:1.25;width:440px}
  .approach__sub{position:absolute;top:470px;left:28px;font-size:14px;color:var(--grey-dark)}

  .social{display:flex;gap:8px}
  .social__dot{width:20px;height:20px;border-radius:50%;background:var(--social)}
  .card--front .social{position:absolute;top:396px;left:600px}

  .url-pill{position:absolute;background:var(--orange);color:#fff;font-weight:600;border-radius:20px;text-align:center}
  .card--front .url-pill{top:432px;left:560px;width:228px;height:34px;line-height:34px;font-size:17px}

  .stamp{position:absolute;top:24px;right:28px;width:82px;height:96px;border:2px dashed #bdbdbd}

  .benefits{position:absolute;top:104px;left:0;width:470px;height:310px;background:linear-gradient(90deg,var(--orange) 0%,var(--orange-light) 100%);padding:22px 28px;color:#fff}
  .benefits__title{font-size:22px;font-weight:600;line-height:1.3}
  .benefits__list{list-style:none;margin-top:16px}
  .benefits__item{display:flex;align-items:center;gap:10px;font-size:14px;line-height:1.55}
  .benefits__item svg{flex:none}

  .card--back .url-pill{top:430px;left:28px;width:230px;height:34px;line-height:34px;font-size:17px}
  .card--back .social{position:absolute;top:437px;left:290px}
</style>
</head>
<body>

<section class="card card--front">
  <div class="brand"><span class="brand__mark"></span><span class="brand__name">Trelvany</span></div>
  <p class="tagline">BRING YOUR BUSINESS TO LIFE</p>

  <div class="hero">
    <div class="hero__photo" role="img" aria-label="Photo of a desk with a business plan notebook and laptop, in orange tones"></div>
    <div class="hero__tint"></div>
    <div class="hero__copy">
      <p>Trelvany helps you create a plan that you can execute easily and implement success year after year. But we don't stop there. Join the Trelvany community and give yourself access to the resources, relationships, and tools that you need to take your career to the next level.</p>
      <p class="hero__lead">The typical business plan fails for one of four reasons:</p>
    </div>
    <div class="reasons">
      <div class="reason">
        <div class="reason__icon"><svg width="40" height="40" viewBox="0 0 40 40" fill="none" stroke="#fff" stroke-width="2.5"><path d="M20 6v26M10 22l10 10 10-10"/></svg></div>
        <p class="reason__text">There are too many goals</p>
      </div>
      <div class="reason">
        <div class="reason__icon"><svg width="42" height="36" viewBox="0 0 42 36" fill="#fff"><path d="M2 6h14l4 4h20v22H2z"/></svg></div>
        <p class="reason__text">It does not connect to actual goals</p>
      </div>
      <div class="reason">
        <div class="reason__icon"><svg width="42" height="36" viewBox="0 0 42 36" fill="none" stroke="#fff" stroke-width="2.5"><path d="M3 3v30h36"/><path d="M8 10l9 9 6-5 12 12"/></svg></div>
        <p class="reason__text">It is too complex to execute easily</p>
      </div>
      <div class="reason">
        <div class="reason__icon"><svg width="40" height="40" viewBox="0 0 40 40" fill="none" stroke="#fff" stroke-width="2.5"><circle cx="20" cy="20" r="16"/><path d="M20 10v10l7 5"/></svg></div>
        <p class="reason__text">There is no timeline or accountability</p>
      </div>
    </div>
  </div>

  <p class="approach">Trelvany takes a fresh approach to business planning.</p>
  <p class="approach__sub">Ready to build a better business? Trelvany can help.</p>
  <div class="social"><span class="social__dot"></span><span class="social__dot"></span><span class="social__dot"></span><span class="social__dot"></span></div>
  <p class="url-pill">www.trelvany.com</p>
</section>

<section class="card card--back">
  <div class="brand"><span class="brand__mark"></span><span class="brand__name">Trelvany</span></div>
  <div class="stamp"></div>

  <div class="benefits">
    <h2 class="benefits__title">Why does running a business have to be so difficult? It doesn't.</h2>
    <ul class="benefits__list">
      <li class="benefits__item"><svg width="13" height="11" viewBox="0 0 13 11" fill="none" stroke="#fff" stroke-width="2"><path d="M1 6l4 4 7-9"/></svg>Learn Business Strategy</li>
      <li class="benefits__item"><svg width="13" height="11" viewBox="0 0 13 11" fill="none" stroke="#fff" stroke-width="2"><path d="M1 6l4 4 7-9"/></svg>Create an Executable Business Plan</li>
      <li class="benefits__item"><svg width="13" height="11" viewBox="0 0 13 11" fill="none" stroke="#fff" stroke-width="2"><path d="M1 6l4 4 7-9"/></svg>Receive Consistent Coaching</li>
      <li class="benefits__item"><svg width="13" height="11" viewBox="0 0 13 11" fill="none" stroke="#fff" stroke-width="2"><path d="M1 6l4 4 7-9"/></svg>Attend Additional Educational Sessions</li>
      <li class="benefits__item"><svg width="13" height="11" viewBox="0 0 13 11" fill="none" stroke="#fff" stroke-width="2"><path d="M1 6l4 4 7-9"/></svg>Profit from Peer Collaboration</li>
      <li class="benefits__item"><svg width="13" height="11" viewBox="0 0 13 11" fill="none" stroke="#fff" stroke-width="2"><path d="M1 6l4 4 7-9"/></svg>Stay Accountable through Bi-Weekly Meetings</li>
      <li class="benefits__item"><svg width="13" height="11" viewBox="0 0 13 11" fill="none" stroke="#fff" stroke-width="2"><path d="M1 6l4 4 7-9"/></svg>Increase your income through Referrals</li>
    </ul>
  </div>

  <p class="url-pill">www.trelvany.com</p>
  <div class="social"><span class="social__dot"></span><span class="social__dot"></span><span class="social__dot"></span><span class="social__dot"></span></div>
</section>

</body>
</html>
```